Harbin Controls Company brochure (For promotion to our clients- Architects, Consultants, designers)

Brief update!!
We want a general Company overview brochure for this particular project, with 3 brochure design projects more to follow later. If we have to up the budget we can look at that depending on the design offering.
1. General overview brochure (this project- approx. 15-20 pages)
to contain 'about us' 1 page, 'what we do' 1 page, 'culture' 1 page, 'experience' 1 page, 'projects' 3 pages , 'lighting control' 2 pages, 'stage control' 1 page 'LED Solutions' 1 page, 'software' 1 page, 'Service' 1 page - front and cover -2 pages.

We wish to produce a brochure to outline the company's background and design philosophy, our products, service and technology. Our company (Australian owned/based) is a leading designer and manufacturer of control technologies (Lighting, LED, Stage) for the Arts, Cultural and Entertainment industry. We would like to produce a brochure design that is inline with our online presence (please see our website www.harbincontrols.example) and uses predominantly imagery in a clever and clean manner.

Target Market(s)

Theatre planners/Consultants, Architects, Electrical/mechanical Consultants, Lighting designers, Integrators, Venue management, technical staff and operatorsw

Industry/Entity Type

It Company

Font styles to use
Other font styles liked:
• Arial or similar - modern and minimal font

Colors
ec1f27
abd037
9acb3c
000000
7f7f7f
606060
b2b2b2
ffffff
00a990

Requirements
Must have
• Striking Product image on Cover (Arty, as website promo banner image)
• Use of Marlow Concert hall exterior image in 'service' section
• Heavy use of venue imagery and well place images of products.
• We imagine a MAX OF 15 to 20 PAGES. This will be used as a stand alone brochure and as part of a binder.
• 'About us' section
• 'What we do' section
• 'Our technology' section
• 'Projects' section (3 pages)
• 'Lighting Control' section
• 'Stage Control' section
• 'Software' section
• 'LED Solutions' section
• 'Service' section
Nice to have
• Clean minimal feel, use of sketch designs of our products (can be made available)
• Close up arty shots of the lighting product on the cover
Should not have
• TBA as we progress

```html
<!DOCTYPE html>
<html lang="en">
<head>
<meta charset="utf-8">
<title>Harbin Controls – What We Do</title>
<link rel="stylesheet" href="https://fonts.googleapis.com/css2?family=Oswald:wght@500&family=Archivo+Black&family=Nunito+Sans:wght@400;700&display=swap">
<style>
  :root {
    --paper: #ffffff;
    --page: #f9b471;
    --ink: #3a2413;
    --heading: #5a3312;
    --ribbon: #5b3310;
    --icon: #3d3a38;
    --white: #ffffff;
  }
  * { box-sizing: border-box; margin: 0; padding: 0; }
  html, body { width: 1200px; height: 1000px; overflow: hidden; background: var(--paper); }
  body { position: relative; font-family: "Nunito Sans", Arial, sans-serif; color: var(--ink); }

  .spread {
    position: absolute; left: 28px; top: 77px; width: 1130px; height: 799px;
    background: var(--page);
    box-shadow: 0 2px 10px rgba(0,0,0,.35);
  }
  .section-ribbon { position: absolute; left: 16px; top: 0; width: 62px; height: 87px; }
  .section-ribbon span {
    position: absolute; left: 0; top: 10px; width: 62px; text-align: center;
    font-family: "Oswald", sans-serif; font-weight: 500; font-size: 44px; line-height: 1; color: var(--white);
  }
  .title-block { position: absolute; left: 93px; top: 86px; width: 315px; }
  .title-block .rule { height: 2px; background: var(--heading); }
  .title-block h1 {
    font-family: "Archivo Black", sans-serif; font-weight: 400; font-size: 35px; line-height: 42px;
    color: var(--heading); letter-spacing: -0.3px; padding: 2px 0 0;
  }
  .intro {
    position: absolute; left: 93px; top: 155px; width: 328px;
    font-size: 11.3px; line-height: 17px;
  }
  .venue-photo {
    position: absolute; left: 441px; top: 0; width: 689px; height: 373px;
    background:
      linear-gradient(90deg, rgba(214,160,110,.85) 0, rgba(214,160,110,.85) 123px, transparent 123px),
      radial-gradient(ellipse at 70% 30%, #e0925a 0%, #a24a22 40%, #4a1a0c 100%);
  }
  .service { position: absolute; width: 490px; }
  .service .icon { position: absolute; left: 0; top: 0; width: 50px; height: 50px; }
  .service h2 { font-size: 13px; line-height: 17px; font-weight: 700; color: var(--heading); margin-left: 57px; }
  .service p { font-size: 11.3px; line-height: 17px; margin-left: 57px; }
  .service p + p { margin-top: 17px; }
  .folio {
    position: absolute; top: 756px; height: 43px;
    font-family: "Oswald", sans-serif; font-weight: 500; font-size: 22px; line-height: 43px; color: var(--white);
  }
  .folio::after { content: ""; position: absolute; top: 0; width: 1px; height: 43px; background: var(--white); }
  .folio.left { left: 16px; } .folio.left::after { left: 28px; }
  .folio.right { left: 1090px; } .folio.right::after { left: -5px; }
</style>
</head>
<body>
<div class="spread">
  <div class="section-ribbon">
    <svg width="62" height="87" viewBox="0 0 62 87"><polygon points="0,0 62,0 62,87 31,73 0,87" fill="var(--ribbon)"/></svg>
    <span>02</span>
  </div>

  <div class="title-block">
    <div class="rule"></div>
    <h1>WHAT WE DO</h1>
    <div class="rule"></div>
  </div>

  <p class="intro">With over 30 years’ experience of designing and installing world class control solutions and having worked on some of the world’s most prestigious Arts &amp; Cultural projects, Harbin Controls has naturally built a passionate team of highly skilled people who love what they do. From lighting/LED control solutions through to stage control and bespoke control systems Harbin Controls is perfectly placed to provide a turnkey control solution for any project specification or size, whilst also providing ongoing service options to suit all.</p>

  <div class="venue-photo" role="img" aria-label="Concert hall interior with warm timber balconies, a pipe organ and an orchestra performing to a full audience"></div>

  <section class="service" style="left:36px; top:397px;">
    <svg class="icon" viewBox="0 0 50 50" fill="none" stroke="var(--icon)" stroke-width="2.5">
      <rect x="1.5" y="1.5" width="47" height="47" rx="6"/>
      <path d="M14 9v32M25 9v32M36 9v32"/>
      <rect x="10.5" y="14" width="7" height="8" fill="var(--icon)"/>
      <rect x="21.5" y="26" width="7" height="8" fill="var(--icon)"/>
      <rect x="32.5" y="17" width="7" height="8" fill="var(--icon)"/>
    </svg>
    <h2>Lighting Control Systems</h2>
    <p>Revolutionary Control technologies to suit all applications : HWT (Harmonic Wave Technology) – APC (Advance phase control) – SPC (Standard Phase Control) – RPC (Reverse Phase Control)</p>
    <p>These technologies are applied to a wide range of HC lighting products and control systems: Series H90, H70, H40 (Modular Cabinets) – Series 10, 5 (Modular 19” Rack Mount) – Series Breeze PC (Wallmount/Rackmount ) – Series Hush (Quiet Dimmers).</p>
  </section>

  <section class="service" style="left:36px; top:553px;">
    <svg class="icon" viewBox="0 0 50 50" fill="none" stroke="var(--icon)" stroke-width="2.5">
      <rect x="1.5" y="1.5" width="47" height="47" rx="6"/>
      <path d="M22 8v20"/>
      <path d="M9 33l24-12c4-2 8 1 8 5s-3 6-6 7l-22 8z"/>
      <ellipse cx="12" cy="37" rx="3" ry="4"/>
    </svg>
    <h2>Stage Machinery control systems</h2>
    <p>The Harbin flying system and stage machinery control can be used on small to large theatres, bespoke projects such as touring shows and major events. Our stage control services cover the full project life cycle: from project planning, delivery to installation, and ongoing support. The key focus points of our stage control team are always Safety, Energy efficiency, Quality, Reliability, Bespoke.</p>
  </section>

  <section class="service" style="left:36px; top:677px;">
    <svg class="icon" viewBox="0 0 50 50" fill="none" stroke="var(--icon)" stroke-width="2.5">
      <rect x="1.5" y="1.5" width="47" height="47" rx="6"/>
      <path d="M20 7v10M30 7v10"/>
      <path d="M14 17h22v8a11 11 0 0 1-22 0z" fill="var(--icon)"/>
      <path d="M25 36v8"/>
    </svg>
    <h2>LED Solutions/Control</h2>
    <p>The FluxLED Driver and the LUMEN-Air LED house light solution have been installed in some of the worlds most prestigious venues providing them with seamless LED control in demanding and dynamic production environments.</p>
  </section>

  <section class="service" style="left:602px; top:397px; width:500px;">
    <svg class="icon" viewBox="0 0 50 50" fill="none" stroke="var(--icon)" stroke-width="2.5">
      <rect x="1.5" y="1.5" width="47" height="47" rx="6"/>
      <path d="M10 10l9 9M14 8l-6 6"/>
      <path d="M19 19l20 20" stroke-width="4"/>
      <path d="M40 10a7 7 0 0 0-9 9L11 39l3 3 20-20a7 7 0 0 0 9-9l-4 4-3-3z" fill="var(--icon)"/>
    </svg>
    <h2>Service and Maintenance</h2>
    <p>HC Service’s highly trained Engineers are renowned for exceeding customer expectations. With our high levels of expertise, 24/7 availability and global mobility, we offer the very best service and support to the customer, every time. We provide a quality international service facility providing:</p>
    <p>– 24 hour support for lighting and stage automation systems. – Highly trained and experienced personnel available to act as a resident service and maintenance option within a customer premises.</p>
    <p>– Programmed Preventative Maintenance and Support. – Equipment repairs and upgrades. – Technical and Operator Training.</p>
  </section>

  <section class="service" style="left:602px; top:620px; width:500px;">
    <svg class="icon" viewBox="0 0 50 50" fill="none" stroke="var(--icon)" stroke-width="2.5">
      <rect x="1.5" y="1.5" width="47" height="47" rx="6"/>
      <circle cx="31" cy="18" r="9" stroke-dasharray="4 3" stroke-width="5"/>
      <circle cx="31" cy="18" r="3"/>
      <circle cx="16" cy="34" r="7" stroke-dasharray="3 3" stroke-width="5"/>
      <circle cx="16" cy="34" r="2"/>
    </svg>
    <h2>OEM</h2>
    <p>Harbin Controls work with other companies to add our pioneering control technology to enhance their products or systems. For further details on our companies OEM capabilities please contact our sales dept.</p>
  </section>

  <div class="folio left">04</div>
  <div class="folio right">05</div>
</div>
</body>
</html>
```